A Real Estate Company Needs a Business Card Design

We need a business card design for a new company based in Boston MA called "Brellmont Real Estate LLC" we are a small company but we like a big corporate look, a simple, sleek, modern and progressive look. we would like the option of having a design that could include the real estate agents personal photo and also a design if the realtor decides not to have a photo. we do not have LOGO at this moment, please use any property look pic corporate with word" Brellmont Real Estate LLC" please see attached file as an example.

```html
<!DOCTYPE html>
<html lang="en">
<head>
<meta charset="utf-8">
<title>Brellmont Real Estate LLC – Business Card</title>
<link rel="stylesheet" href="https://fonts.googleapis.com/css2?family=Open+Sans:wght@400;700&display=swap">
<style>
  :root {
    --backdrop: #4b5059;
    --lime: #b7bc32;
    --ocean: #1a6f9c;
    --ocean-deep: #1b6896;
    --white: #ffffff;
    --photo-light: #c9b2a3;
    --photo-dark: #4a4546;
  }
  * { margin: 0; padding: 0; box-sizing: border-box; }
  html, body { width: 1200px; height: 685px; overflow: hidden; }
  body {
    position: relative;
    background: var(--backdrop);
    font-family: "Open Sans", Arial, sans-serif;
    color: var(--white);
  }
  .card {
    position: absolute;
    top: 187px;
    width: 529px;
    height: 301px;
    box-shadow: 0 4px 10px rgba(0,0,0,.35);
  }
  .card--front { left: 63px; background: var(--lime); }
  .card--back  { left: 609px; background: var(--ocean); }

  .brand__mark { position: absolute; display: block; }
  .brand__name {
    position: absolute;
    display: block;
    font-weight: 700;
    text-transform: uppercase;
    white-space: nowrap;
  }
  .brand__line--main { display: block; }
  .brand__line--sub { display: block; }

  /* front */
  .card--front .brand__mark {
    left: 87px; top: 96px; width: 92px; height: 92px;
    background: var(--ocean);
  }
  .card--front .brand__name { left: 192px; top: 136px; color: var(--ocean-deep); }
  .card--front .brand__line--main { font-size: 30px; line-height: 32px; letter-spacing: 1px; }
  .card--front .brand__line--sub  { font-size: 17px; line-height: 22px; letter-spacing: 3.4px; }

  /* back */
  .card--back .brand__mark {
    left: 330px; top: 38px; width: 116px; height: 116px;
    background: var(--white);
  }
  .card--back .brand__name {
    left: 289px; width: 200px; top: 172px;
    text-align: center; color: var(--white);
  }
  .card--back .brand__line--main { font-size: 22px; line-height: 24px; letter-spacing: 1px; }
  .card--back .brand__line--sub  { font-size: 13px; line-height: 18px; letter-spacing: 2.6px; }

  .agent__photo {
    position: absolute;
    left: 39px; top: 36px;
    width: 84px; height: 84px;
    border-radius: 50%;
    border: 2px solid var(--white);
    background: linear-gradient(180deg, var(--photo-light) 0%, var(--photo-light) 55%, var(--photo-dark) 100%);
  }
  .agent__name {
    position: absolute; left: 39px; top: 128px;
    font-size: 21px; font-weight: 400; line-height: 28px;
  }
  .agent__details {
    position: absolute; left: 40px; top: 161px;
    list-style: none; font-size: 13px; line-height: 17.5px;
  }
  .card__rule {
    position: absolute; left: 36px; top: 240px;
    width: 456px; height: 1.5px; background: var(--white);
  }
  .card__address {
    position: absolute; left: 0; right: 0; top: 258px;
    text-align: center; font-size: 15px;
  }
</style>
</head>
<body>
  <section class="card card--front" aria-label="Card front">
    <span class="brand__mark"></span>
    <span class="brand__name">
      <span class="brand__line--main">Brellmont</span>
      <span class="brand__line--sub">Real Estate LLC</span>
    </span>
  </section>

  <section class="card card--back" aria-label="Card back">
    <div class="agent__photo" role="img" aria-label="Portrait photo of the real estate agent"></div>
    <h1 class="agent__name">Daniel Harlow</h1>
    <ul class="agent__details">
      <li>Real Estate Agent</li>
      <li>09090 555 218</li>
      <li>dharlow@brellmont.com</li>
    </ul>
    <span class="brand__mark"></span>
    <span class="brand__name">
      <span class="brand__line--main">Brellmont</span>
      <span class="brand__line--sub">Real Estate LLC</span>
    </span>
    <div class="card__rule"></div>
    <p class="card__address">PO Box 31-402, Ridgefield, Boston MA 02118, USA</p>
  </section>
</body>
</html>
```